Candle company needs a label for candle

Looking for a designer to create my candle label. I am going to attach a few pictures of my vision for the label as well as my Company Logo and jar I have puchased. I'm going for the modern rustic feel but you are the designer and have full trust in your abilities. The label is going to be printed on Kraft paper (2x3) so looking for the font to be black. The candle label MUST include the following information:
Candle Birchway Co.
NO. 01: Eucalyptus + Spearmint
Handmade In NJ
Soy Wax
9oz

Industry/Entity Type

Candle Industry

Colors

Designer to choose colors to be used in the design.

Requirements
Should not have
• Any images

```html
<!DOCTYPE html>
<html lang="en">
<head>
<meta charset="utf-8">
<title>Candle Birchway Co. — No. 01 Label</title>
<link rel="stylesheet" href="https://fonts.googleapis.com/css2?family=Cinzel:wght@400&family=Montserrat:wght@400&display=swap">
<style>
  :root {
    --page-bg: #e4e4e4;
    --label-light: #faf5e6;
    --label-mid: #efe2bd;
    --label-warm: #e2cf98;
    --ink: #1c1c1c;
  }
  * { box-sizing: border-box; margin: 0; padding: 0; }
  html, body {
    width: 1200px;
    height: 622px;
    overflow: hidden;
    background: var(--page-bg);
  }
  .canvas {
    position: relative;
    width: 1200px;
    height: 622px;
  }
  .label {
    position: absolute;
    left: 170px;
    top: 24px;
    width: 860px;
    height: 574px;
    border-radius: 22px;
    overflow: hidden;
    color: var(--ink);
    background:
      radial-gradient(ellipse 55% 45% at 78% 72%, var(--label-warm) 0%, rgba(226,207,152,0) 70%),
      radial-gradient(ellipse 40% 35% at 20% 30%, var(--label-mid) 0%, rgba(239,226,189,0) 75%),
      radial-gradient(ellipse 50% 40% at 65% 15%, var(--label-light) 0%, rgba(250,245,230,0) 80%),
      linear-gradient(160deg, var(--label-mid) 0%, var(--label-light) 45%, var(--label-mid) 75%, var(--label-warm) 100%);
    box-shadow: 0 1px 3px rgba(0,0,0,0.12);
  }
  .brand-name {
    position: absolute;
    left: 55px;
    top: 150px;
    font-family: "Montserrat", sans-serif;
    font-weight: 400;
    font-size: 30px;
    line-height: 1.2;
    color: var(--ink);
  }
  .product-number {
    position: absolute;
    left: 53px;
    top: 300px;
    font-family: "Cinzel", serif;
    font-weight: 400;
    font-size: 78px;
    line-height: 1;
  }
  .scent {
    position: absolute;
    left: 55px;
    top: 388px;
    font-family: "Cinzel", serif;
    font-size: 22px;
    letter-spacing: 0.01em;
  }
  .details {
    position: absolute;
    left: 55px;
    top: 470px;
    list-style: none;
    font-family: "Montserrat", sans-serif;
    font-size: 17px;
    line-height: 24px;
  }
  .description {
    position: absolute;
    left: 484px;
    top: 206px;
    width: 320px;
    text-align: center;
    font-family: "Montserrat", sans-serif;
    font-size: 17px;
    line-height: 24px;
  }
</style>
</head>
<body>
  <main class="canvas">
    <section class="label">
      <p class="brand-name">Candle Birchway Co.</p>
      <h1 class="product-number">NO. 01</h1>
      <p class="scent">Eucalyptus + Spearmint</p>
      <ul class="details">
        <li>Handmade In NJ</li>
        <li>Soy Wax</li>
        <li>9oz</li>
      </ul>
      <p class="description">Lorem Ipsum is simply dummy text of the printing and typesetting industry. Lorem Ipsum has been the industry's standard dummy text ever since the 1500s, when an unknown printer took a galley of type and scrambled it to make a type specimen book.</p>
    </section>
  </main>
</body>
</html>
```